Web form face-lift for an online startup

We are a web startup building a SaaS application for the freight industry. The project is mainly dedicated to the paint the main form that our customer are using along the search results that the they get. All details are in the attached documents.
Updates
The application serves the Freight Forwarders community so please think towards this industry when using background images, banners, colors, icons, etc. Computer and technology images are irrelevant.
Customer fields at the top of the page is actually part of the form.
Target Market(s)
Usually business users (Sales people, procurement, shippers, freight forwarders). Some are less tech savvy and some appreciate the new trendy web apps.
Industry/Entity Type
Building
Colors
Designer to choose colors to be used in the design.
Look and feel
Each slider illustrates characteristics of the customer's brand and the style your logo design should communicate.

```html
<!DOCTYPE html>
<html lang="en">
<head>
<meta charset="utf-8">
<title>SaaS Application – Search For Quotes</title>
<link href="https://fonts.googleapis.com/css2?family=Open+Sans:wght@400;600;700&family=Noto+Serif:wght@400&display=swap" rel="stylesheet">
<style>
:root{
  --navy-900:#17283d;
  --navy-800:#1e344f;
  --navy-700:#243f60;
  --navy-600:#2c4a6e;
  --page:#f5f5f5;
  --panel:#eeeeee;
  --panel-line:#dddddd;
  --field-line:#c9c9c9;
  --text:#555555;
  --heading:#1d3049;
  --white:#ffffff;
  --crate:#d9903f;
  --boxes:#c8312a;
  --mail:#d8d8d8;
  --alert:#d02a2a;
  --link-blue:#8fb1d6;
}
*{box-sizing:border-box;margin:0;padding:0}
html,body{width:1189px;height:1200px;overflow:hidden;background:var(--page)}
body{font-family:"Open Sans",Arial,sans-serif;color:var(--text)}
.stage{position:absolute;left:0;top:0;width:1000px;height:1009px;transform:scale(1.189);transform-origin:0 0;background:var(--page)}
.abs{position:absolute}

/* header */
.utility-bar{left:0;top:0;width:1000px;height:32px;background:var(--navy-900);font-size:12px;color:var(--link-blue)}
.utility-bar span{position:absolute;top:10px}
.caret{display:inline-block;margin-left:6px;border:4px solid transparent;border-top:5px solid currentColor;border-bottom:0;vertical-align:2px}
.masthead{left:0;top:32px;width:1000px;height:74px;background:linear-gradient(var(--navy-700),var(--navy-800));border-top:1px solid #34557c}
.brand{left:20px;top:54px;font-family:"Noto Serif",Georgia,serif;font-size:27px;color:var(--white)}
.nav-home{left:352px;top:63px;width:42px;height:43px;background:var(--white);border-radius:3px 3px 0 0}
.nav-item{top:63px;width:141px;height:43px;background:linear-gradient(var(--navy-600),var(--navy-800));border:1px solid #0f1e30;border-bottom:0;border-radius:3px 3px 0 0;color:var(--white);font-size:12px;font-weight:700;text-align:center;line-height:43px}

/* form head */
.page-title{left:40px;top:135px;font-size:19px;font-weight:600;color:var(--heading);display:flex;align-items:center;gap:6px}
.label{font-size:14px;color:var(--text)}
.field{background:var(--white);border:1px solid var(--field-line);font-size:14px;color:var(--text);padding:0 9px;display:flex;align-items:center}
.field.center{justify-content:center;padding:0}
.field.select{justify-content:space-between}
.field.select::after{content:"";border:4px solid transparent;border-top:5px solid #444;border-bottom:0}
.check{width:11px;height:11px;border:1px solid #bbb;border-radius:2px;background:#f4f4f4}
.radio{width:14px;height:14px;border:1px solid #bbb;border-radius:50%;background:linear-gradient(#fafafa,#ddd)}

/* tabs */
.tab{top:256px;width:108px;height:58px;border:1px solid #d6d6d6;border-bottom:0;border-radius:3px 3px 0 0;background:#ececec;display:flex;align-items:center;justify-content:center}
.tab.active{background:linear-gradient(var(--navy-600),var(--navy-800));border-color:#0f1e30}
.tab-art{width:40px;height:38px;border-radius:3px}
.btn{background:linear-gradient(var(--navy-600),var(--navy-900));border:1px solid #0c1828;border-radius:3px;color:var(--white);font-weight:600;display:flex;align-items:center;justify-content:center;gap:6px}
.panel{left:38px;top:314px;width:917px;height:576px;background:var(--panel);border:1px solid var(--panel-line);border-radius:3px}
.col-head{top:340px;font-size:14px;color:var(--text)}
.rule{left:52px;width:885px;height:1px;background:#cfcfcf;border-bottom:1px solid #fafafa}
.options-title{left:57px;top:649px;font-size:13px;font-weight:700;color:#444}
.link{font-size:13px;font-weight:700;color:var(--heading)}

/* footer */
.footer{left:0;top:943px;width:1000px;height:66px;background:var(--navy-800);border-top:2px solid var(--navy-900);color:var(--white);font-size:13px;font-weight:600}
.footer nav{position:absolute;top:24px;display:flex;gap:8px}
.footer nav b{font-weight:400}
</style>
</head>
<body>
<div class="stage">

  <header>
    <div class="abs utility-bar">
      <span style="left:777px">USD<i class="caret"></i></span>
      <span style="left:842px">English<i class="caret"></i></span>
      <span style="left:915px">Username</span>
    </div>
    <div class="abs masthead"></div>
    <div class="abs brand">SaaS Application</div>
    <div class="abs nav-home">
      <svg width="42" height="43" viewBox="0 0 42 43" aria-label="Dashboard">
        <circle cx="21" cy="22" r="10" fill="none" stroke="#1d3049" stroke-width="2.5"/>
        <path d="M15 22a6 6 0 0 1 12 0" fill="none" stroke="#1d3049" stroke-width="1.5" stroke-dasharray="1.5 1.5"/>
        <path d="M21 24 L25 17" stroke="#1d3049" stroke-width="2" stroke-linecap="round"/>
        <circle cx="21" cy="24" r="1.8" fill="#1d3049"/>
      </svg>
    </div>
    <div class="abs nav-item" style="left:400px">Menu Item 1<i class="caret"></i></div>
    <div class="abs nav-item" style="left:546px">Menu Item 2<i class="caret"></i></div>
    <div class="abs nav-item" style="left:692px">Menu Item 3<i class="caret"></i></div>
    <div class="abs nav-item" style="left:838px">Menu Item 4<i class="caret"></i></div>
  </header>

  <main>
    <h1 class="abs page-title">
      <svg width="24" height="20" viewBox="0 0 24 20"><circle cx="8" cy="8" r="5.5" fill="none" stroke="#1d3049" stroke-width="2.5"/><path d="M12 12 L20 18" stroke="#1d3049" stroke-width="3.5" stroke-linecap="round"/></svg>
      Search For Quotes
    </h1>
    <div class="abs label" style="left:40px;top:179px">Customer</div>
    <div class="abs field" style="left:124px;top:174px;width:271px;height:29px"></div>
    <div class="abs check" style="left:125px;top:213px"></div>
    <div class="abs label" style="left:143px;top:209px">Rate Quote ?</div>

    <div class="abs tab active" style="left:53px"><div class="tab-art" role="img" aria-label="Wooden crate illustration" style="background:linear-gradient(#e8a755,var(--crate))"></div></div>
    <div class="abs tab" style="left:171px"><div class="tab-art" role="img" aria-label="Boxes on a pallet illustration" style="width:50px;background:linear-gradient(#dd4a40,var(--boxes))"></div></div>
    <div class="abs tab" style="left:291px"><div class="tab-art" role="img" aria-label="Envelope and pencil illustration" style="width:52px;height:32px;background:linear-gradient(#f2f2f2,var(--mail))"></div></div>
    <div class="abs btn" style="left:882px;top:270px;width:60px;height:31px;font-size:14px">More</div>

    <section class="abs panel"></section>

    <div class="abs col-head" style="left:66px">Qty</div>
    <div class="abs col-head" style="left:123px">Stacklabel</div>
    <div class="abs col-head" style="left:212px">Load</div>
    <div class="abs col-head" style="left:507px">Length</div>
    <div class="abs col-head" style="left:591px">Width</div>
    <div class="abs col-head" style="left:674px">Height</div>
    <div class="abs col-head" style="left:812px">Weight</div>

    <div class="abs field center" style="left:54px;top:366px;width:49px;height:29px">5</div>
    <div class="abs check" style="left:148px;top:375px"></div>
    <div class="abs field select" style="left:212px;top:366px;width:271px;height:29px">Box/ Pallet</div>
    <div class="abs field center" style="left:493px;top:366px;width:74px;height:29px">100</div>
    <div class="abs field center" style="left:577px;top:366px;width:74px;height:29px">100</div>
    <div class="abs field center" style="left:660px;top:366px;width:74px;height:29px">100</div>
    <div class="abs field select" style="left:741px;top:366px;width:49px;height:29px;padding:0 6px">cm</div>
    <div class="abs field center" style="left:798px;top:366px;width:74px;height:29px">100</div>
    <div class="abs field select" style="left:880px;top:366px;width:49px;height:29px;padding:0 8px">kg</div>

    <div class="abs btn" style="left:65px;top:427px;width:144px;height:32px;font-size:14px">
      <svg width="12" height="12" viewBox="0 0 12 12"><path d="M6 1v10M1 6h10" stroke="#fff" stroke-width="2.5"/></svg>Add More Units
    </div>

    <div class="abs rule" style="top:477px"></div>

    <div class="abs label" style="left:517px;top:502px">Total</div>
    <div class="abs field center" style="left:563px;top:496px;width:74px;height:29px">5</div>
    <div class="abs field center" style="left:643px;top:496px;width:74px;height:29px">1</div>
    <div class="abs field select" style="left:716px;top:496px;width:74px;height:29px;padding:0 8px 0 15px">CBM</div>
    <div class="abs field center" style="left:798px;top:496px;width:74px;height:29px">100</div>
    <div class="abs field select" style="left:880px;top:496px;width:49px;height:29px;padding:0 8px">kg</div>

    <div class="abs rule" style="top:547px"></div>

    <div class="abs label" style="left:58px;top:577px">From</div>
    <div class="abs field" style="left:111px;top:573px;width:271px;height:29px">Shipping address or port</div>
    <div class="abs label" style="left:631px;top:577px">To</div>
    <div class="abs field" style="left:664px;top:573px;width:271px;height:29px">Shipping address or port</div>

    <div class="abs options-title">OPTIONS</div>
    <div class="abs radio" style="left:68px;top:682px"></div>
    <div class="abs label" style="left:90px;top:680px">Import</div>
    <div class="abs radio" style="left:150px;top:682px"></div>
    <div class="abs label" style="left:172px;top:680px">Export</div>
    <div class="abs label" style="left:264px;top:680px">Incotem: FCA</div>

    <div class="abs check" style="left:395px;top:684px"></div>
    <svg class="abs" style="left:411px;top:678px" width="21" height="21" viewBox="0 0 21 21"><circle cx="10.5" cy="10.5" r="8.5" fill="#fff" stroke="var(--alert)" stroke-width="2.2"/><rect x="6" y="7" width="9" height="7" rx="1" fill="#2a5aa0"/><path d="M4.5 16.5 16.5 4.5" stroke="var(--alert)" stroke-width="2.2"/></svg>
    <div class="abs check" style="left:448px;top:684px"></div>
    <svg class="abs" style="left:465px;top:678px" width="21" height="21" viewBox="0 0 21 21"><circle cx="10.5" cy="10.5" r="8.5" fill="#fff" stroke="var(--alert)" stroke-width="2.2"/><circle cx="10.5" cy="10.5" r="4" fill="#2a5aa0"/><path d="M4.5 16.5 16.5 4.5" stroke="var(--alert)" stroke-width="2.2"/></svg>
    <div class="abs check" style="left:500px;top:684px"></div>
    <svg class="abs" style="left:518px;top:678px" width="21" height="21" viewBox="0 0 21 21"><circle cx="10.5" cy="10.5" r="8.5" fill="#fff" stroke="var(--alert)" stroke-width="2.2"/><path d="M6 13 10 8 14 11" fill="none" stroke="#2a5aa0" stroke-width="2"/><path d="M4.5 16.5 16.5 4.5" stroke="var(--alert)" stroke-width="2.2"/></svg>

    <div class="abs field select" style="left:664px;top:676px;width:271px;height:29px;padding:0 14px 0 8px">Price Level</div>
    <div class="abs link" style="left:846px;top:735px">More Options</div>

    <div class="abs btn" style="left:396px;top:795px;width:203px;height:40px;font-size:17px;gap:8px">
      <svg width="24" height="20" viewBox="0 0 24 20"><circle cx="8" cy="8" r="5.5" fill="none" stroke="#fff" stroke-width="2.5"/><path d="M12 12 L20 18" stroke="#fff" stroke-width="3.5" stroke-linecap="round"/></svg>Search Quotes
    </div>
    <div class="abs label" style="left:638px;top:805px">or</div>
    <div class="abs link" style="left:667px;top:803px;font-size:15px">Create manually</div>
  </main>

  <footer class="abs footer">
    <nav style="left:49px"><span>About Us</span><b>|</b><span>Privacy Policy</span><b>|</b><span>Terms Of Service</span><b>|</b><span>News</span></nav>
    <nav style="left:759px"><span>Blog</span><b>|</b><span>Socialnest</span><b>|</b><span>Chirpline</span></nav>
  </footer>

</div>
</body>
</html>
```